Indigenous Mentoring Masterclass

We are a small Indigenous owned company that specializes in mentoring training for anybody who mentors Indigenous mentees: www.tarnlee.com.au

We would like a brochure advertising an upcoming training course being held Parramatta, Sydney, NSW. The brochure should show the course goals and objectives (course syllabus attached)

The brochure to have colouring similar to loggo attached.

The final design should advertise a sharp two day course delivered by specialist Indigenous trainers.
Updates

Hi Everyone,

Hi Res Loggo updated for your use.  Please let me know if you require further help.

Regards

Target Market(s)

Anybody working in the Indigenous Australian domain.

Industry/Entity Type

Advertising

Requirements
Must have
• This new and improved skills - based course has been sharpened to a 2 day program to focus mentors on deep mentoring and therefore creating transformational changes with mentees.

Brochure will have a focus on the trainer capability.

Our Trainers
Under the leadership of TKO’s remarkably accomplished Directors Harriet Dunmore and Gordon Pelkin, the company has gained a reputation across a range of organisations and sectors as a dependable supplier of superior cutting-edge training, facilitation and consultative services, consistently providing the greatest value for money.
The TKO team is made up of highly qualified and practiced individuals with a passion and commitment to providing fresh, innovative and proven approaches to effective training delivery and group facilitation. We are self-motivated and results-focused individuals who achieve proven results for our clients. TKO’s Directors bring together highly competent project teams to achieve proven specific client objectives. These teams can comprise of a number of expert associates in relevant specialist fields, and are linked in to help do so. You will have an opportunity to spend two days with these Directors and ask how you can leverage your mentoring skills within your organization.
TKOs Business lines: agile and scrum, tribal leadership, global diversity and sustainability, culture hacking, leadership, community and organization development, change, coaching and mentoring.

Learning Objectives
After completing the course, you will learn powerful new distinctions that will improve your knowledge and practice base to leverage your mentoring conversations.
Learn practical problem solving and solution focused methods to address mentee concerns and understand and manage moods with yourself, mentees and others.

Learning Goals

To appreciate the power of language and conversations in getting work done, discuss with other like-minded participants the uncertainty of change and how it impacts Indigenous Australians.

Please note: picture of Harriet and Gordon attached as the couple.
Nice to have
• Loggo
Your ideas and creativity based on the course syllabus
An editable document so that I can insert and or change venue details whenever I deliver training in another state.

REGISTRATION DETAILS

enquiries to Harriet Dunmore 1800 947 315

COMPANY DETAILS

www.tarnlee.com.au
PO Box 836, Wyong, NSW 2259

```html
<!DOCTYPE html>
<html lang="en">
<head>
<meta charset="utf-8">
<title>Indigenous Mentoring Masterclass – Brochure Spread</title>
<link href="https://fonts.googleapis.com/css2?family=Quicksand:wght@300;400&family=Arimo:wght@400&display=swap" rel="stylesheet">
<style>
  :root {
    --sun: #fdcb12;
    --ochre: #c57a00;
    --earth-red: #9a001b;
    --ink: #1a1a1a;
    --cream: #fbe9c4;
    --paper: #ffffff;
  }
  * { margin: 0; padding: 0; box-sizing: border-box; }
  html, body { width: 1200px; height: 900px; overflow: hidden; background: var(--paper); }
  .canvas { position: relative; width: 1200px; height: 900px; }
  .spread {
    position: absolute; left: 33px; top: 55px; width: 1135px; height: 802px;
    border: 1px solid var(--ink); overflow: hidden; background: var(--paper);
  }
  .pattern-band {
    position: absolute; height: 50px; border-radius: 25px;
    background: linear-gradient(90deg, var(--sun) 0%, var(--earth-red) 35%, var(--ochre) 65%, var(--sun) 85%, var(--earth-red) 100%);
    opacity: 0.9;
  }
  .pattern-band--top { left: 3px; top: 11px; width: 558px; }
  .pattern-band--bottom { left: 573px; top: 740px; width: 558px; }
  .panel { position: absolute; display: flex; align-items: center; justify-content: center; text-align: center; }
  .panel--intro { left: 567px; top: 0; width: 568px; height: 402px; background: var(--ochre); }
  .panel--venue { left: 0; top: 592px; width: 567px; height: 210px; background: var(--earth-red); }
  .panel-text {
    font-family: "Quicksand", sans-serif; font-weight: 300; color: var(--cream);
    font-size: 20px; line-height: 24.5px; letter-spacing: 0.3px;
  }
  .panel--intro .panel-text { margin-top: -2px; }
  .panel--venue .panel-text { color: #f3e4e0; font-size: 20.5px; line-height: 25px; margin-top: 3px; }
  .pull-quote {
    position: absolute; left: 26px; top: 123px; width: 238px; text-align: center;
    font-family: "Quicksand", sans-serif; font-weight: 300; color: var(--earth-red);
    font-size: 21px; line-height: 25.8px;
  }
  .body-copy {
    position: absolute; width: 240px;
    font-family: "Arimo", Arial, sans-serif; font-size: 14px; line-height: 20.5px; color: var(--ink);
  }
  .team-intro { left: 300px; top: 88px; }
  .leadership { left: 33px; top: 339px; }
  .directors { left: 300px; top: 339px; }
  .objective-text { left: 597px; top: 481px; }
  .goal-text { left: 878px; top: 481px; }
  .section-title {
    position: absolute; width: 260px; text-align: center;
    font-family: "Quicksand", sans-serif; font-weight: 400; color: var(--earth-red);
    font-size: 21.5px; line-height: 26px;
  }
  .objective-title { left: 576px; top: 430px; }
  .goal-title { left: 858px; top: 430px; }
</style>
</head>
<body>
<div class="canvas">
  <div class="spread">
    <div class="pattern-band pattern-band--top" role="img" aria-label="Decorative row of yellow, red and ochre dots"></div>

    <p class="pull-quote">“...with a passion<br>and commitment to<br>providing fresh,<br>innovative and proven<br>approaches to<br>effective training...”</p>

    <p class="body-copy team-intro">The TKO team is made up of<br>highly qualified and practiced<br>individuals with a passion and<br>commitment to providing fresh, in-<br>novative and proven approaches<br>to effective training delivery and<br>group facilitation. We are self-<br>motivated and results-focused<br>individuals who achieve proven<br>results for our clients.</p>

    <p class="body-copy leadership">Under the leadership of TKO’s<br>remarkably accomplished Direc-<br>tors Harriet Dunmore and Gordon<br>Pelkin, the company has gained<br>a reputation across a range of<br>organisations and sectors as a<br>dependable supplier of superior<br>cutting-edge training, facilitation<br>and consultative services, consist-<br>ently providing the greatest value<br>for money.</p>

    <p class="body-copy directors">TKO’s Directors bring together<br>highly competent project teams<br>to achieve proven specific client<br>objectives. These teams can com-<br>prise of a number of expert asso-<br>ciates in relevant specialist fields.<br>You will have an opportunity to<br>spend two days with these Direc-<br>tors and ask how you can lever-<br>age your mentoring skills within<br>your organization.</p>

    <section class="panel panel--intro">
      <p class="panel-text">This new and improved skills-based<br>course has been sharpened to a 2 day<br>program to focus mentors on deep<br>mentoring, creating transformational<br>changes with mentees.</p>
    </section>

    <section class="panel panel--venue">
      <p class="panel-text">Don’t miss our upcoming training course:<br>Parramatta, Sydney, NSW.</p>
    </section>

    <h2 class="section-title objective-title">Learning Objective:</h2>
    <p class="body-copy objective-text">After completing the course, you<br>will learn powerful new distinctions<br>that will improve your knowledge<br>and practice base to leverage<br>your mentoring conversations.<br>Learn practical problem solving<br>and solution focused methods to<br>address mentee concerns and un-<br>derstand and manage moods with<br>yourself, mentees and others.</p>

    <h2 class="section-title goal-title">Learning Goal:</h2>
    <p class="body-copy goal-text">To appreciate the power of<br>language and conversations in<br>getting work done, discuss with<br>other like-minded participants the<br>uncertainty of change and how it<br>impacts Indigenous Australians.</p>

    <div class="pattern-band pattern-band--bottom" role="img" aria-label="Decorative row of yellow, red and ochre dots"></div>
  </div>
</div>
</body>
</html>
```